Tranquil Pathway Business Card

Logo attached. (will be printing onto thick white/off white textured card)

Double sided business card for two Therapists working at Tranquil Pathway.

Require one design, but with different name and mobile numbers on each card.

Target Market(s)

Medical, Health

Industry/Entity Type

Business

Contact Information for Business Card

Need one business card design, but a separate card for each person - Colin Marchetti and Marieke de Boeckx.

FRONT OF CARD

Logo

Name (Colin Marchetti on one card, Marieke de Boeckx on the other)
Professional Clinical Hypnotherapist

Consulting Rooms (Near Lindqvist Hospital)
482 Brackenfield Road
Dunmore VIC 3987

Colin@TranquilPathway.example.au OR Marieke@TranquilPathway.example.au

Mobile: 0455 872 604 (for Colin) OR
Mobile: 0467 290 518 (for Marieke)

BACK OF CARD

Logo

Website: www.TranquilPathway.example.au

Phone: 1300 958 471

Requirements
Must have
• Text and logo only. No additiional graphics.

```html
<!DOCTYPE html>
<html lang="en">
<head>
<meta charset="utf-8">
<title>Tranquil Pathway Business Card</title>
<link rel="stylesheet" href="https://fonts.googleapis.com/css2?family=Montserrat:wght@400;500;700&family=Mulish:wght@400;500&display=swap">
<style>
  :root {
    --page: #e4e4e6;
    --navy: #232a6e;
    --navy-deep: #1b2158;
    --navy-light: #2f3a8c;
    --ink-grey: #555a62;
    --label-grey: #8a8fae;
    --white: #ffffff;
    --paper-tint: #f3f3f5;
  }
  * { box-sizing: border-box; margin: 0; padding: 0; }
  html, body {
    width: 960px; height: 1200px; overflow: hidden;
    background: var(--page);
  }
  .canvas { position: relative; width: 960px; height: 1200px; }

  .card {
    position: absolute; left: 132px; width: 696px; height: 450px;
    overflow: hidden;
    box-shadow: 0 3px 10px rgba(0,0,0,0.18);
  }
  .card-front { top: 100px; background: var(--white); }
  .card-back  { top: 658px; background: linear-gradient(180deg, var(--navy-light) 0%, var(--navy) 45%, var(--navy-deep) 100%); }

  .texture { position: absolute; inset: 0; }
  .card-front .texture { background: linear-gradient(135deg, var(--white) 0%, var(--paper-tint) 100%); }
  .card-back .texture { background: radial-gradient(ellipse at 50% 30%, rgba(255,255,255,0.05), rgba(255,255,255,0) 70%); }

  .edge-band { position: absolute; left: 0; top: 0; bottom: 0; width: 7px; background: var(--navy); }

  .brand { position: absolute; display: flex; align-items: center; font-family: "Montserrat", sans-serif; font-weight: 700; text-transform: uppercase; }
  .brand-mark { border-radius: 50%; flex: none; }
  .card-front .brand { right: 52px; top: 38px; gap: 16px; color: var(--navy); font-size: 22px; letter-spacing: 0.5px; }
  .card-front .brand-mark { width: 82px; height: 82px; background: var(--navy); }
  .card-back .brand { left: 76px; top: 104px; gap: 34px; color: var(--white); font-size: 42px; line-height: 1.05; letter-spacing: 1px; }
  .card-back .brand-mark { width: 172px; height: 172px; background: var(--white); }

  .person { position: absolute; left: 58px; top: 170px; font-family: "Mulish", sans-serif; }
  .person-name { font-family: "Montserrat", sans-serif; font-weight: 700; font-size: 25px; color: var(--navy); }
  .person-role { font-size: 19px; color: var(--navy); margin-top: 4px; }
  .address { position: absolute; left: 58px; top: 256px; font-family: "Mulish", sans-serif; font-size: 19px; line-height: 28px; color: var(--ink-grey); }
  .address small { font-size: 14px; }

  .contact { position: absolute; font-family: "Mulish", sans-serif; display: grid; grid-template-columns: auto 1fr; align-items: baseline; }
  .card-front .contact { left: 58px; top: 364px; column-gap: 18px; row-gap: 4px; }
  .card-front .contact dt { font-size: 14px; color: var(--navy); }
  .card-front .contact dd { font-size: 20px; color: var(--navy); }
  .card-back .contact { left: 77px; top: 332px; column-gap: 28px; row-gap: 4px; }
  .card-back .contact dt { font-size: 21px; color: var(--label-grey); }
  .card-back .contact dd { font-size: 21px; color: var(--white); }
</style>
</head>
<body>
<main class="canvas">
  <section class="card card-front" aria-label="Card front">
    <div class="texture" role="img" aria-label="Soft wave background texture"></div>
    <div class="edge-band"></div>
    <div class="brand"><span class="brand-mark"></span><span class="brand-name">Tranquil Pathway</span></div>
    <div class="person">
      <h1 class="person-name">Colin Marchetti</h1>
      <p class="person-role">Professional Clinical Hypnotherapist</p>
    </div>
    <address class="address" style="font-style:normal">
      Consulting Rooms <small>(Near Lindqvist Hospital)</small><br>
      482 Brackenfield Road<br>
      Dunmore VIC 3987
    </address>
    <dl class="contact">
      <dt>E-mail:</dt><dd>Colin@TranquilPathway.example.au</dd>
      <dt>Mobile:</dt><dd>0455 872 604</dd>
    </dl>
  </section>

  <section class="card card-back" aria-label="Card back">
    <div class="texture" role="img" aria-label="Soft wave background texture"></div>
    <div class="brand"><span class="brand-mark"></span><span class="brand-name">Tranquil<br>Pathway</span></div>
    <dl class="contact">
      <dt>Website:</dt><dd>www.TranquilPathway.example.au</dd>
      <dt>Phone:</dt><dd>1300 958 471</dd>
    </dl>
  </section>
</main>
</body>
</html>
```